Grand Opening of Rusty's Tap, a craft beer bar in mountains of Payson AZ. Rusty is our black lab.

We need a card designed to advertise the grand opening of Rusty's Tap. It is a craft beer bar (we do not make our own beer but will highlight local beer) located next to Pinecrest Lanes (which has also been rebranded). We will be serving craft beer and spirited drinks, along with a great burger (Rusty's Melt) and other bar food. The interior is a little industrial (corregated metal bar front) with a warm feel. We are trying to appeal to a more upscale crowd without being snobby. We would like it to be family friendly during the day.

Reason: I'm extending the deadline by 1 day so I have time to review updates. Thank you all for submissions!

```html
<!DOCTYPE html>
<html lang="en">
<head>
<meta charset="utf-8">
<title>Rusty's Tap – Grand Opening</title>
<link rel="stylesheet" href="https://fonts.googleapis.com/css2?family=Alegreya+SC:wght@500;700&family=New+Rocker&display=swap">
<style>
  :root {
    --wood-dark: #4a2c18;
    --wood-mid: #7a4f31;
    --wood-light: #8e5f3d;
    --metal-dark: #7d8287;
    --metal-light: #c9ccce;
    --gold-dark: #9a6a16;
    --gold: #d9a636;
    --gold-light: #f4d27a;
    --plaque-black: #141414;
    --plaque-grey: #3a3a3a;
    --cream: #f3ecd4;
    --white: #ffffff;
  }
  * { margin: 0; padding: 0; box-sizing: border-box; }
  html, body { width: 1200px; height: 800px; overflow: hidden; background: #222; }
  .card {
    position: relative;
    width: 1200px;
    height: 800px;
    overflow: hidden;
    font-family: "Alegreya SC", Georgia, serif;
    color: var(--white);
  }
  .wood-wall {
    position: absolute; inset: 0;
    background: linear-gradient(90deg, var(--wood-dark), var(--wood-light) 25%, var(--wood-mid) 50%, var(--wood-light) 75%, var(--wood-dark));
  }
  .metal-band {
    position: absolute; left: 0; width: 1200px;
    background: linear-gradient(180deg, var(--metal-light), var(--metal-dark) 50%, var(--metal-light));
  }
  .metal-band--top { top: 0; height: 150px; }
  .metal-band--bottom { top: 690px; height: 110px; }
  .wheat {
    position: absolute;
    border-radius: 60px;
    background: linear-gradient(180deg, var(--cream), var(--gold-light) 60%, var(--gold));
  }
  .wheat--left { left: 62px; top: 345px; width: 120px; height: 350px; transform: rotate(8deg); }
  .wheat--right { left: 1015px; top: 345px; width: 120px; height: 345px; transform: rotate(-8deg); }
  .shapes { position: absolute; inset: 0; }
  .headline {
    position: absolute; left: 300px; top: 48px; width: 600px;
    text-align: center; font-size: 74px; font-weight: 500; line-height: 112px;
    letter-spacing: 1px;
  }
  .bar-name {
    position: absolute; left: 0; top: 195px; width: 1200px;
    text-align: center; font-family: "New Rocker", "Times New Roman", serif;
    font-size: 136px; line-height: 140px; letter-spacing: 6px;
  }
  .date-main {
    position: absolute; left: 398px; top: 362px; width: 408px;
    text-align: center; font-size: 46px; font-weight: 700; line-height: 50px;
  }
  .date-time {
    position: absolute; left: 398px; top: 420px; width: 408px;
    text-align: center; font-size: 22px; font-weight: 700; line-height: 26px;
  }
  .lineup {
    position: absolute; left: 0; top: 512px; width: 1200px;
    text-align: center; font-size: 31px; line-height: 37px; font-weight: 500;
  }
  .specials {
    position: absolute; left: 392px; top: 698px; width: 414px;
    text-align: center; font-weight: 500;
  }
  .specials__price { font-size: 29px; line-height: 34px; }
  .specials__more { font-size: 20px; line-height: 26px; }
  .coupon {
    position: absolute; left: 95px; top: 652px; width: 140px;
    text-align: center; font-size: 18px; line-height: 22px; font-weight: 500;
  }
  .validity {
    position: absolute; left: 915px; top: 712px; width: 245px;
    text-align: center; font-size: 25px; line-height: 30px; font-weight: 500;
  }
</style>
</head>
<body>
<div class="card">
  <div class="wood-wall" role="img" aria-label="Warm brown vertical wood plank wall"></div>
  <div class="metal-band metal-band--top" role="img" aria-label="Corrugated metal panel"></div>
  <div class="metal-band metal-band--bottom" role="img" aria-label="Corrugated metal panel"></div>
  <div class="wheat wheat--left" role="img" aria-label="Golden wheat sprig decoration"></div>
  <div class="wheat wheat--right" role="img" aria-label="Golden wheat sprig decoration"></div>

  <svg class="shapes" width="1200" height="800" viewBox="0 0 1200 800" aria-hidden="true">
    <defs>
      <linearGradient id="gold" x1="0" y1="0" x2="0" y2="1">
        <stop offset="0" stop-color="#f4d27a"/>
        <stop offset="0.5" stop-color="#b8801e"/>
        <stop offset="1" stop-color="#f0c862"/>
      </linearGradient>
      <linearGradient id="plaque" x1="0" y1="0" x2="1" y2="0">
        <stop offset="0" stop-color="#141414"/>
        <stop offset="0.5" stop-color="#3a3a3a"/>
        <stop offset="1" stop-color="#141414"/>
      </linearGradient>
    </defs>

    <!-- top plaque -->
    <rect x="285" y="28" width="630" height="154" rx="77" fill="url(#gold)"/>
    <rect x="297" y="40" width="606" height="130" rx="65" fill="url(#plaque)"/>
    <g fill="#e9c46a">
      <circle cx="345" cy="38" r="5"/><circle cx="592" cy="38" r="5"/><circle cx="855" cy="38" r="5"/>
      <circle cx="345" cy="172" r="5"/><circle cx="592" cy="172" r="5"/><circle cx="855" cy="172" r="5"/>
      <circle cx="289" cy="102" r="5"/><circle cx="908" cy="102" r="5"/>
    </g>

    <!-- date ribbon -->
    <polygon points="312,368 430,368 430,488 322,518 355,440" fill="#222" stroke="url(#gold)" stroke-width="6" stroke-linejoin="round"/>
    <polygon points="888,368 770,368 770,488 878,518 845,440" fill="#222" stroke="url(#gold)" stroke-width="6" stroke-linejoin="round"/>
    <rect x="398" y="342" width="408" height="136" fill="url(#plaque)" stroke="url(#gold)" stroke-width="7"/>

    <!-- specials pill -->
    <rect x="390" y="677" width="418" height="100" rx="50" fill="url(#gold)"/>
    <rect x="399" y="686" width="400" height="82" rx="41" fill="url(#plaque)"/>

    <!-- coupon starburst -->
    <polygon points="275,705 250,728 260,760 227,767 220,800 188,790 165,815 142,790 110,800 103,767 70,760 80,728 55,705 80,682 70,650 103,643 110,610 142,620 165,595 188,620 220,610 227,643 260,650 250,682" fill="url(#gold)"/>
    <polygon transform="translate(165 705) scale(0.9) translate(-165 -705)" points="275,705 250,728 260,760 227,767 220,800 188,790 165,815 142,790 110,800 103,767 70,760 80,728 55,705 80,682 70,650 103,643 110,610 142,620 165,595 188,620 220,610 227,643 260,650 250,682" fill="url(#plaque)"/>
  </svg>

  <h2 class="headline">Grand Opening</h2>
  <h1 class="bar-name">RUSTY'S TAP</h1>
  <p class="date-main">September 19th</p>
  <p class="date-time">at 4pm.</p>

  <p class="lineup">
    Entertainment by:<br>
    Ridgeline Five on Friday night<br>
    Dale Whitmore &amp; the Copper Kettles<br>
    on Saturday night and Sunday afternoon.
  </p>

  <div class="specials">
    <p class="specials__price">$3 Craft beers</p>
    <p class="specials__more">and drink specials all weekend</p>
  </div>

  <p class="coupon">BUY ONE SANDWICH GET ONE 50% OFF COUPON</p>

  <p class="validity">Card valid from:<br>9/19 to 9/21.</p>
</div>
</body>
</html>
```